Brenwick Drilling Inc. Business card design

Business card design for "Brenwick Drilling Inc. - Directional Drilling Services"

Address is:

Brenwick Drilling Inc.
512 - 73 Tolvane Crescent SW
Calgary, Alberta, Canada
T2K 4P8

Please incorporate the logo design into the card, thank you.

Target Market(s)

Oil & Gas and Drilling

Industry/Entity Type

Business

```html
<!DOCTYPE html>
<html lang="en">
<head>
<meta charset="utf-8">
<title>Brenwick Drilling Inc. – Business Card</title>
<link rel="stylesheet" href="https://fonts.googleapis.com/css2?family=Ubuntu:wght@400;500;700&display=swap">
<style>
  :root {
    --canvas: #e4e5e7;
    --card-black: #0c0c0d;
    --band-black: #1b1b1d;
    --brand-red: #e02b2b;
    --brand-orange: #f7941d;
    --accent-grey: #b9babd;
    --accent-white: #ffffff;
    --text-white: #ffffff;
    --text-grey: #8d8e92;
  }
  * { box-sizing: border-box; margin: 0; padding: 0; }
  html, body { width: 1200px; height: 1000px; overflow: hidden; }
  body {
    background: var(--canvas);
    font-family: "Ubuntu", Arial, sans-serif;
    position: relative;
  }
  .card {
    position: absolute;
    width: 540px;
    height: 320px;
    border-radius: 22px;
    overflow: hidden;
    background: var(--card-black);
    box-shadow: 0 18px 40px rgba(0,0,0,.25);
  }
  .card-front { left: 50px; top: 190px; }
  .card-back { left: 610px; top: 490px; }

  .edge-stripes {
    position: absolute; top: 0; bottom: 0;
    display: flex;
  }
  .edge-stripes span { display: block; height: 100%; }
  .edge-left { left: 0; }
  .edge-right { right: 0; }
  .stripe-orange { width: 16px; background: var(--brand-orange); }
  .stripe-red { width: 10px; background: var(--brand-red); }
  .stripe-white { width: 6px; background: var(--accent-white); }
  .stripe-grey { width: 12px; background: var(--accent-grey); }

  .brand-lockup {
    position: absolute;
    left: 26px; right: 18px; top: 110px;
    display: flex; flex-direction: column; align-items: center;
    color: var(--text-white);
  }
  .brand-row { display: flex; align-items: center; gap: 14px; }
  .brand-mark {
    width: 22px; height: 22px; border-radius: 50%;
    background: var(--brand-red);
  }
  .brand-name {
    font-weight: 700; font-size: 28px; letter-spacing: 1px;
    text-transform: uppercase; color: var(--text-white);
  }
  .brand-tagline {
    margin-top: 6px;
    font-weight: 400; font-size: 12.5px; letter-spacing: 4px;
    text-transform: uppercase; color: var(--text-white);
  }
  .web-address {
    position: absolute; right: 56px; bottom: 34px;
    font-size: 14px; letter-spacing: .5px; color: var(--text-grey);
  }

  .contact-band {
    position: absolute; left: 0; right: 0; top: 30px; height: 110px;
    background: var(--band-black);
  }
  .contact-person {
    position: absolute; left: 40px; top: 50px; color: var(--text-white);
  }
  .person-name { font-weight: 500; font-size: 19px; color: var(--brand-red); }
  .person-role { font-size: 13px; margin-top: 4px; }
  .contact-lines {
    position: absolute; left: 260px; top: 52px;
    font-size: 13px; line-height: 1.45; color: var(--text-white);
  }
  .company-address {
    position: absolute; left: 40px; top: 180px;
    font-size: 13.5px; line-height: 1.4; color: var(--text-white);
  }
  .company-name {
    font-weight: 500; font-size: 14.5px; color: var(--brand-red);
    text-transform: uppercase; margin-bottom: 6px;
  }
</style>
</head>
<body>

<section class="card card-front" aria-label="Business card front">
  <div class="edge-stripes edge-left" aria-hidden="true">
    <span class="stripe-orange"></span><span class="stripe-red"></span>
  </div>
  <div class="edge-stripes edge-right" aria-hidden="true">
    <span class="stripe-white"></span><span class="stripe-grey"></span>
  </div>
  <div class="brand-lockup">
    <div class="brand-row">
      <div class="brand-mark"></div>
      <div class="brand-name">Brenwick Drilling Inc.</div>
    </div>
    <div class="brand-tagline">Directional Drilling Services</div>
  </div>
  <div class="web-address">www.BrenwickDrilling.com</div>
</section>

<section class="card card-back" aria-label="Business card back">
  <div class="contact-band" aria-hidden="true"></div>
  <div class="edge-stripes edge-right" aria-hidden="true">
    <span class="stripe-grey"></span><span class="stripe-white"></span><span class="stripe-red"></span><span class="stripe-orange"></span>
  </div>
  <div class="contact-person">
    <div class="person-name">Colin Marsh</div>
    <div class="person-role">Accountant</div>
  </div>
  <div class="contact-lines">
    <div>+1 403 555 0182</div>
    <div>colin@BrenwickDrilling.com</div>
  </div>
  <div class="company-address">
    <div class="company-name">Brenwick Drilling Inc.</div>
    <div>512 - 73 Tolvane Crescent SW</div>
    <div>Calgary, Alberta, Canada</div>
    <div>T2K 4P8</div>
  </div>
</section>

</body>
</html>
```